Brackenfield Security Store Signage with provided LOGO

Need 2 designs (1) indicating the store is around the corner horizontal format and (1) in a vertical format without the around the corner indication. HD image for a 24" by 60" sign. Use attached image for inspiration. Our business of on the south side of a large building and we need to have 2 signs on the front of the build indicating LEFT and the last sign will be a sidewalk sign next to our business.
Updates

Project Deadline Extended
Reason: Allow a couple more designer to sumbit

Industry/Entity Type

Security

Font styles to use
Serif

Colors
33a6d7

Requirements
Must have
• WEBSITE URL: www.vaultwardstation.com and www.brackenfieldsecuritystore.com they can be in small font.
Nice to have
• Phone Number (855) 316-2984

```html
<!DOCTYPE html>
<html lang="en">
<head>
<meta charset="utf-8">
<title>Brackenfield Security Store Signage</title>
<link rel="stylesheet" href="https://fonts.googleapis.com/css2?family=Oswald:wght@600&family=Roboto:wght@300;400&display=swap">
<style>
  :root {
    --bg: #e9e9ea;
    --blue-top: #2a8fd6;
    --blue-bottom: #1a4c9e;
    --brand-blue: #1f6fc4;
    --ink: #111111;
    --white: #ffffff;
  }
  html, body {
    margin: 0;
    padding: 0;
    width: 1200px;
    height: 1200px;
    overflow: hidden;
    background: var(--bg);
  }
  .canvas {
    position: relative;
    width: 1200px;
    height: 1200px;
  }
  .sign {
    position: absolute;
    height: 412px;
    box-shadow: 0 8px 22px rgba(0,0,0,0.25);
    overflow: hidden;
  }
  .sign--corner { left: 43px; top: 134px; width: 1062px; }
  .sign--sidewalk { left: 142px; top: 652px; width: 1030px; }
  .sign__backdrop {
    position: absolute;
    inset: 0;
    width: 100%;
    height: 100%;
  }
  .contact {
    position: absolute;
    text-align: center;
    color: var(--white);
    font-family: "Roboto", Arial, sans-serif;
  }
  .contact__phone {
    font-weight: 300;
    font-size: 44px;
    letter-spacing: 1px;
    line-height: 1;
    margin: 0 0 10px;
  }
  .contact__url {
    font-weight: 400;
    font-size: 18px;
    line-height: 24px;
    margin: 0;
  }
  .sign--corner .contact { left: 61px; width: 320px; top: 86px; }
  .sign--sidewalk .contact { left: 589px; width: 380px; top: 108px; }
  .direction-arrow {
    position: absolute;
    left: 73px;
    top: 226px;
    width: 294px;
    height: 62px;
  }
  .brand {
    position: absolute;
    display: flex;
    align-items: center;
    gap: 18px;
  }
  .sign--corner .brand { left: 503px; top: 118px; }
  .sign--sidewalk .brand { left: 56px; top: 128px; }
  .brand__dot {
    width: 118px;
    height: 118px;
    border-radius: 50%;
    background: var(--brand-blue);
    flex: none;
  }
  .brand__name {
    font-family: "Oswald", "Arial Narrow", sans-serif;
    font-weight: 600;
    font-size: 46px;
    line-height: 1.05;
    color: var(--brand-blue);
    text-transform: uppercase;
    margin: 0;
  }
</style>
</head>
<body>
<main class="canvas">

  <section class="sign sign--corner" aria-label="Around the corner sign">
    <svg class="sign__backdrop" viewBox="0 0 1062 412" preserveAspectRatio="none" aria-hidden="true">
      <defs>
        <linearGradient id="blueFadeCorner" x1="0" y1="0" x2="0" y2="1">
          <stop offset="0" stop-color="var(--blue-top)"/>
          <stop offset="1" stop-color="var(--blue-bottom)"/>
        </linearGradient>
      </defs>
      <rect width="1062" height="412" fill="url(#blueFadeCorner)"/>
      <path d="M504 0 Q382 206 516 412 L530 412 Q408 206 518 0 Z" fill="var(--ink)"/>
      <path d="M518 0 Q408 206 530 412 L1062 412 L1062 0 Z" fill="var(--white)"/>
    </svg>

    <div class="contact">
      <p class="contact__phone">(855) 316-2984</p>
      <p class="contact__url">www.vaultwardstation.com</p>
      <p class="contact__url">www.brackenfieldsecuritystore.com</p>
    </div>

    <svg class="direction-arrow" viewBox="0 0 294 62" aria-label="Arrow pointing left">
      <polygon points="0,31 36,0 36,18 294,18 294,44 36,44 36,62" fill="var(--white)"/>
      <rect x="58" y="18" width="5" height="26" fill="var(--blue-top)"/>
      <rect x="70" y="18" width="5" height="26" fill="var(--blue-top)"/>
      <rect x="82" y="18" width="5" height="26" fill="var(--blue-top)"/>
      <rect x="238" y="18" width="5" height="26" fill="var(--blue-bottom)"/>
      <rect x="250" y="18" width="5" height="26" fill="var(--blue-bottom)"/>
      <rect x="262" y="18" width="5" height="26" fill="var(--blue-bottom)"/>
    </svg>

    <div class="brand">
      <span class="brand__dot" aria-hidden="true"></span>
      <p class="brand__name">Brackenfield<br>Security Store</p>
    </div>
  </section>

  <section class="sign sign--sidewalk" aria-label="Sidewalk sign">
    <svg class="sign__backdrop" viewBox="0 0 1030 412" preserveAspectRatio="none" aria-hidden="true">
      <defs>
        <linearGradient id="blueFadeSidewalk" x1="0" y1="0" x2="0" y2="1">
          <stop offset="0" stop-color="var(--blue-top)"/>
          <stop offset="1" stop-color="var(--blue-bottom)"/>
        </linearGradient>
      </defs>
      <rect width="1030" height="412" fill="var(--white)"/>
      <path d="M516 0 Q640 206 516 412 L1030 412 L1030 0 Z" fill="url(#blueFadeSidewalk)"/>
      <path d="M500 0 Q628 206 502 412 L516 412 Q640 206 516 0 Z" fill="var(--ink)"/>
    </svg>

    <div class="brand">
      <span class="brand__dot" aria-hidden="true"></span>
      <p class="brand__name">Brackenfield<br>Security Store</p>
    </div>

    <div class="contact">
      <p class="contact__phone">(855) 316-2984</p>
      <p class="contact__url">www.vaultwardstation.com</p>
      <p class="contact__url">www.brackenfieldsecuritystore.com</p>
    </div>
  </section>

</main>
</body>
</html>
```